Dorvelan Swimming & Athletics Center

We need Business Card for a Athletics center
The logo frome the Uploaded Files ( b card fimal)
Οn one side of card we need the logo of company the Contact and the website:
1. Address:(Limassol, Cyprus 12-14 Stavrinelou str,Ano Trimeni,P.C. 4832)

2.Phone number: (+357) 25-704263

3. Mail: info@dorvelanfit.example

3. Website: www.dorvelanfit.example

Οn the other side of the card we need to write the sport of the company:

1. Artistic Gymnastics
2. Swimming
3. Gym - Fitness
4. Programs
5. Dancing
5.Tennis

From the Uploaded Files you can get the logo.In a logo is behind the black color which can be removed from logo.

Υou can use that color you want.
.
Updates

Industry/Entity Type

Business

Font styles to use
Decorative

Colors
0555a3
ffcf3e
3176b5
0692cd
add136
f04a50
000000
cfcfcf
9d9d9d

Requirements
Should not have
• photos with faces
• photo fro the Website:www.dorvelanfit.example

```html
<!DOCTYPE html>
<html lang="en">
<head>
<meta charset="utf-8">
<title>Dorvelan Swimming &amp; Athletics Center – Business Card</title>
<link rel="stylesheet" href="https://fonts.googleapis.com/css2?family=Open+Sans:wght@300;400;800&display=swap">
<style>
  :root {
    --page: #ffffff;
    --black: #000000;
    --logo-bg: #161616;
    --gold: #ffcf3e;
    --gold-deep: #f5b21c;
    --frame: #555555;
    --grey-light: #cfcfcf;
    --grey-mid: #9d9d9d;
    --ink: #1e1e1e;
    --list-ink: #d6d6d6;
    --map-base: #e6e2d9;
  }
  * { margin: 0; padding: 0; box-sizing: border-box; }
  html, body {
    width: 1200px;
    height: 1002px;
    overflow: hidden;
    background: var(--page);
    font-family: "Open Sans", Arial, sans-serif;
  }
  .canvas { position: relative; width: 1200px; height: 1002px; }

  .card {
    position: absolute;
    left: 262px;
    width: 673px;
    height: 380px;
    border: 3px solid var(--frame);
    overflow: hidden;
  }
  .card--front { top: 93px; background: var(--black); }
  .card--back  { top: 545px; background: var(--black); }

  /* Front */
  .front-art { position: absolute; inset: 0; }
  .logo-plate {
    position: absolute;
    left: 130px; top: 44px;
    width: 427px; height: 90px;
    background: var(--logo-bg);
    display: flex; align-items: center; justify-content: center; gap: 22px;
  }
  .logo-name {
    font-weight: 800;
    font-size: 46px;
    letter-spacing: 3px;
    color: var(--gold-deep);
    line-height: 1;
  }
  .logo-mark {
    width: 62px; height: 62px;
    border-radius: 50%;
    background: var(--gold);
  }
  .contact {
    position: absolute;
    left: 0; right: 0; top: 212px;
    text-align: center;
    color: var(--ink);
    font-size: 16px;
    line-height: 1;
  }
  .contact__line { height: 36px; display: flex; align-items: center; justify-content: center; }
  .contact__phone::before,
  .contact__phone::after {
    content: "";
    display: block;
    width: 176px;
    height: 1.5px;
    background: var(--ink);
  }
  .contact__phone::before { margin-right: 10px; }
  .contact__phone::after { margin-left: 10px; }

  /* Back */
  .sports {
    position: absolute;
    right: 385px; top: 62px;
    list-style: none;
    text-align: right;
  }
  .sports__item {
    height: 42px;
    font-weight: 300;
    font-size: 22px;
    color: var(--list-ink);
    display: flex; align-items: center; justify-content: flex-end;
  }
  .sports__item::after {
    content: "";
    width: 9px; height: 9px;
    margin-left: 18px;
    background: var(--gold);
  }
  .location-map {
    position: absolute;
    left: 344px; top: 0;
    width: 326px; height: 100%;
    background: linear-gradient(160deg, #ebe7de 0%, var(--map-base) 55%, #dcd8cf 100%);
  }
</style>
</head>
<body>
<main class="canvas">

  <section class="card card--front" aria-label="Card front: logo and contact details">
    <svg class="front-art" width="673" height="380" viewBox="0 0 673 380" aria-hidden="true">
      <defs>
        <linearGradient id="panelGrey" x1="0" y1="0" x2="0" y2="1">
          <stop offset="0" stop-color="#cfcfcf"/>
          <stop offset="1" stop-color="#8f8f8f"/>
        </linearGradient>
        <linearGradient id="swoosh" x1="0" y1="0" x2="1" y2="0">
          <stop offset="0" stop-color="#3a3a3a"/>
          <stop offset="1" stop-color="#1a1a1a"/>
        </linearGradient>
      </defs>
      <rect width="673" height="196" fill="#000"/>
      <path d="M0 172 Q330 168 673 140 L673 196 L0 196 Z" fill="url(#swoosh)"/>
      <rect y="196" width="673" height="184" fill="url(#panelGrey)"/>
    </svg>

    <div class="logo-plate">
      <span class="logo-name">DORVELAN</span>
      <span class="logo-mark" aria-hidden="true"></span>
    </div>

    <address class="contact" style="font-style:normal">
      <div class="contact__line">Limassol, Cyprus 12-14 Stavrinelou str,Ano Trimeni,P.C. 4832)</div>
      <div class="contact__line contact__phone">(+357) 25-704263</div>
      <div class="contact__line">info@dorvelanfit.example</div>
      <div class="contact__line">www.dorvelanfit.example</div>
    </address>
  </section>

  <section class="card card--back" aria-label="Card back: sports offered and location map">
    <ul class="sports">
      <li class="sports__item">Artistic Gymnastics</li>
      <li class="sports__item">Swimming</li>
      <li class="sports__item">Gym - Fitness</li>
      <li class="sports__item">Programs</li>
      <li class="sports__item">Dancing</li>
      <li class="sports__item">Tennis</li>
    </ul>
    <div class="location-map" role="img" aria-label="Street map showing the center's location with a map pin"></div>
  </section>

</main>
</body>
</html>
```